Amber Ridge Publishing Web Page Design

Design a website for my new start up publishing company - Amber Ridge Publishing, the first work published by ARP with be a new book by M.R. Theodor called Silent Ledger. The prototype for the book cover is attached.

Target Market(s)

Worldwide, all readers of mystery, fiction, etc.

Industry/Entity Type

Book Publisher

Coding

Coded - Design and coding required

Number of Pages Required

1 page

```html
<!DOCTYPE html>
<html lang="en">
<head>
<meta charset="utf-8">
<title>Amber Ridge Publishing</title>
<link href="https://fonts.googleapis.com/css2?family=Montserrat:wght@400;600;700;800&family=Open+Sans:wght@400;600;700&family=Roboto+Slab:wght@700&display=swap" rel="stylesheet">
<style>
:root{
  --blue:#3b9ad9;
  --blue-dark:#2f86c2;
  --ink:#2a2a2a;
  --text:#555;
  --muted:#8a8a8a;
  --line:#e2e2e2;
  --pale:#f1f1f1;
  --dark:#252525;
  --footer:#1c1c1c;
  --white:#fff;
  --star:#f2b01e;
}
*{box-sizing:border-box;margin:0;padding:0}
html,body{width:1200px;height:4569px;overflow:hidden}
body{font-family:"Open Sans",sans-serif;color:var(--text);font-size:12px;background:var(--white);position:relative}
.wrap{width:740px;margin:0 auto;position:relative}
.section-title{font-family:"Montserrat",sans-serif;font-weight:700;font-size:19px;color:var(--ink);text-align:center;text-transform:uppercase;letter-spacing:.3px}
.section-title .accent{color:var(--blue)}
.title-rule{width:30px;height:2px;background:var(--blue);margin:10px auto 14px}
.section-lead{text-align:center;font-size:10.5px;line-height:1.6;color:var(--muted);width:680px;margin:0 auto}
.btn{display:inline-block;font-family:"Montserrat",sans-serif;font-weight:600;font-size:10px;text-transform:uppercase;padding:8px 16px;border-radius:2px}
.btn-blue{background:var(--blue);color:var(--white)}
.btn-grey{background:#555;color:var(--white)}
.btn-outline{border:1px solid #cfcfcf;color:var(--text)}
.stars{color:var(--star);font-size:10px;letter-spacing:1px}

/* hero */
.hero{height:594px;position:relative;overflow:hidden}
.hero-photo{position:absolute;inset:0;background:linear-gradient(135deg,#3a3633 0%,#58524b 40%,#2e2b28 70%,#4a443d 100%)}
.hero-shade{position:absolute;inset:0;background:rgba(0,0,0,.35)}
.topbar{position:absolute;top:10px;left:0;right:0}
.topbar .wrap{display:flex;justify-content:flex-end;gap:18px;align-items:center;color:#ddd;font-size:10px}
.header{position:absolute;top:32px;left:0;right:0}
.header .wrap{display:flex;align-items:center;justify-content:space-between}
.logo{display:flex;align-items:center;gap:8px;font-family:"Montserrat",sans-serif;font-weight:700;font-size:15px;color:var(--white);text-transform:uppercase;letter-spacing:.5px}
.logo-mark{width:14px;height:14px;background:var(--white)}
.nav{display:flex;gap:26px;font-family:"Montserrat",sans-serif;font-size:11px;color:var(--white)}
.hero-copy{position:absolute;top:150px;left:230px;width:360px;color:var(--white)}
.hero-copy h1{font-family:"Roboto Slab",serif;font-size:42px;line-height:1.1;text-transform:uppercase}
.hero-copy p{font-size:11px;line-height:1.6;color:#ddd;margin:14px 0 18px}
.hero-arrow{position:absolute;top:240px;width:22px;height:40px}
.welcome-bar{position:absolute;bottom:0;left:0;right:0;height:70px;background:rgba(20,20,20,.82)}
.welcome-bar .wrap{height:70px;display:flex;align-items:center;justify-content:space-between}
.welcome-bar h2{font-family:"Montserrat",sans-serif;font-size:14px;color:var(--white);text-transform:uppercase}
.welcome-bar p{font-size:10.5px;color:#bbb;margin-top:4px}
.welcome-bar .actions{display:flex;gap:12px}
.welcome-bar .btn{padding:10px 22px}

/* intro features */
.intro{height:396px;padding-top:50px}
.features{display:flex;gap:20px;margin-top:32px}
.feature{width:170px;height:210px;border:1px solid var(--line);text-align:center;padding:22px 12px}
.feature .icon{width:44px;height:44px;border-radius:50%;background:#ededed;margin:0 auto 12px;display:flex;align-items:center;justify-content:center}
.feature h3{font-family:"Montserrat",sans-serif;font-size:12px;color:var(--ink);font-weight:600;margin-bottom:12px}
.feature p{font-size:10px;line-height:1.6;color:var(--muted);margin-bottom:12px}
.feature .btn{padding:5px 10px;font-size:9px}
.feature.is-active{background:var(--blue);border-color:var(--blue)}
.feature.is-active h3,.feature.is-active p{color:var(--white)}
.feature.is-active .icon{background:rgba(255,255,255,.25)}
.feature.is-active .btn{border-color:#fff;color:#fff}

/* best seller */
.bestseller{height:488px;background:var(--pale);padding-top:38px}
.book-row{display:flex;gap:20px;margin-top:26px}
.book-card{width:170px;height:290px;background:var(--white);padding:14px;position:relative}
.book-cover{height:160px;margin:0 auto 10px;width:110px}
.book-card h4{font-size:11px;color:var(--ink);text-align:center;font-weight:600}
.book-card .by{font-size:9.5px;color:var(--muted);text-align:center;margin-top:3px}
.book-card .meta{display:flex;justify-content:space-between;align-items:center;margin-top:14px}
.book-card .price{font-family:"Montserrat",sans-serif;font-weight:700;color:var(--ink);font-size:13px}
.book-card.is-featured h4{color:var(--blue)}
.book-card .view-more{position:absolute;left:0;right:0;bottom:0;height:28px;background:var(--blue);color:#fff;font-family:"Montserrat",sans-serif;font-size:10px;font-weight:700;display:flex;align-items:center;justify-content:center}
.badge{position:absolute;top:-9px;right:-9px;width:24px;height:24px;border-radius:50%;background:var(--blue);color:#fff;font-size:8px;font-weight:700;display:flex;align-items:center;justify-content:center}
.pager{display:flex;gap:6px;justify-content:center;margin-top:20px}
.pager span{width:14px;height:14px;font-size:8px;background:var(--white);color:var(--text);display:flex;align-items:center;justify-content:center}
.pager span.is-current{background:var(--blue);color:#fff}

/* video */
.video{height:295px;position:relative}
.video-photo{position:absolute;inset:0;background:linear-gradient(100deg,#4d4640 0%,#6b625a 35%,#3b3631 70%,#5a534b 100%)}
.video-shade{position:absolute;inset:0;background:rgba(0,0,0,.35)}
.video-copy{position:relative;text-align:center;padding-top:80px;color:#fff}
.video-copy h2{font-family:"Montserrat",sans-serif;font-size:22px;font-weight:700;text-transform:uppercase;letter-spacing:.5px}
.play{width:40px;height:40px;border-radius:50%;border:2px solid #fff;margin:16px auto 12px;display:flex;align-items:center;justify-content:center}
.video-copy .sub{font-family:"Montserrat",sans-serif;font-size:10px;text-transform:uppercase}
.video-copy .sub small{display:block;font-family:"Open Sans",sans-serif;font-size:9px;color:#ccc;text-transform:none;margin-top:4px}

/* product columns */
.catalog{height:405px;padding-top:44px}
.catalog .wrap{display:flex;gap:40px}
.catalog-col{width:220px}
.catalog-head{display:flex;justify-content:space-between;align-items:center;border-bottom:1px solid var(--line);padding-bottom:8px;margin-bottom:18px}
.catalog-head h3{font-family:"Montserrat",sans-serif;font-size:12px;font-weight:600;color:var(--ink);text-transform:uppercase}
.arrows{display:flex;gap:3px}
.arrows span{width:14px;height:14px;background:#ddd;font-size:9px;display:flex;align-items:center;justify-content:center;color:#666}
.item{display:flex;gap:14px;height:130px;margin-bottom:14px}
.item-cover{width:70px;height:110px;flex:none}
.item h4{font-family:"Montserrat",sans-serif;font-size:10px;color:var(--ink);margin-top:6px}
.item .by{font-size:9px;color:var(--muted);margin:3px 0 5px}
.tag{display:inline-block;background:var(--blue);color:#fff;font-size:9px;font-weight:700;padding:2px 6px;margin:5px 0 12px}
.add{font-family:"Montserrat",sans-serif;font-size:9px;font-weight:600;color:var(--ink)}

/* testimonials */
.testimonials{height:314px;background:var(--dark);padding-top:36px;color:#ccc;text-align:center}
.testimonials .section-title{color:#fff}
.people{display:flex;justify-content:center;align-items:center;gap:22px;margin-top:18px}
.avatar{border-radius:50%;background:linear-gradient(135deg,#a58e7a,#6d5a4b)}
.avatar.sm{width:44px;height:44px;opacity:.7}
.avatar.lg{width:62px;height:62px;border:3px solid #fff}
.nav-arrow{color:#fff;font-size:14px}
.testimonials .name{font-family:"Montserrat",sans-serif;color:var(--blue);font-size:12px;font-weight:700;margin-top:10px;text-transform:uppercase}
.testimonials .role{font-size:9px;color:#999}
.testimonials .quote{font-size:10.5px;line-height:1.6;width:420px;margin:10px auto 0;color:#bbb}
.dots{display:flex;gap:5px;justify-content:center;margin-top:14px}
.dots i{width:6px;height:6px;border-radius:50%;background:#666}
.dots i.is-current{background:#fff}

/* counters */
.counters{height:152px;background:var(--blue)}
.counters .wrap{display:flex;justify-content:space-between;padding:40px 40px 0}
.counter{text-align:center;color:#fff;width:140px}
.counter strong{font-family:"Montserrat",sans-serif;font-size:38px;font-weight:700;display:block;line-height:1}
.counter span{font-family:"Montserrat",sans-serif;font-size:9px;text-transform:uppercase;display:block;margin-top:6px;border-top:1px solid rgba(255,255,255,.4);padding-top:5px}

/* guide */
.guide{height:518px;padding-top:50px}
.guide-grid{display:grid;grid-template-columns:1fr 1fr;gap:20px;margin-top:22px}
.guide-card{display:flex;height:160px;background:var(--pale)}
.guide-cover{width:170px;height:160px;position:relative;flex:none}
.guide-date{position:absolute;right:6px;bottom:14px;font-family:"Montserrat",sans-serif;font-size:30px;color:#999;font-weight:600}
.guide-date i{position:absolute;right:0;bottom:-10px;font-style:normal;background:var(--blue);color:#fff;font-size:8px;padding:1px 5px}
.guide-body{padding:16px 14px}
.guide-body .by{font-size:9px;color:var(--muted)}
.guide-body h4{font-family:"Montserrat",sans-serif;font-size:12px;color:var(--ink);margin:3px 0 10px;text-transform:uppercase}
.guide-body p{font-size:9.5px;line-height:1.6;color:var(--muted)}
.guide-body .more{font-family:"Montserrat",sans-serif;font-size:9px;font-weight:700;color:var(--ink);margin-top:10px;display:block}

/* gift card */
.gift{height:387px;background:linear-gradient(160deg,#3d9cdb 0%,#3d9cdb 55%,#2f8ccc 55%,#3593d3 100%);position:relative;padding-top:30px;color:#fff}
.gift .section-title{color:#fff}
.gift-list{width:380px;margin-top:22px}
.gift-item{margin-bottom:20px;padding:6px 8px}
.gift-item.is-active{background:rgba(255,255,255,.15)}
.gift-item h4{font-family:"Montserrat",sans-serif;font-size:12px;text-transform:uppercase;display:flex;align-items:center;gap:8px}
.gift-item h4 i{width:12px;height:12px;background:#fff;border-radius:2px}
.gift-item p{font-size:9.5px;line-height:1.6;color:#e3f1fb;margin-top:6px}
.gift-visual{position:absolute;left:790px;top:90px;width:400px;height:234px;background:linear-gradient(135deg,#4a4540,#2a2725)}

/* pricing */
.pricing{height:639px;padding-top:56px}
.plans{display:flex;gap:50px;margin-top:26px}
.plan{width:213px;height:344px;background:var(--pale);text-align:center}
.plan-head{background:#777;color:#fff;font-family:"Montserrat",sans-serif;font-size:14px;font-weight:700;height:66px;padding-top:16px;text-transform:uppercase}
.plan-price{width:66px;height:66px;border-radius:50%;background:#fff;border:3px solid var(--pale);margin:-24px auto 10px;display:flex;flex-direction:column;align-items:center;justify-content:center;font-family:"Montserrat",sans-serif;color:var(--ink)}
.plan-price strong{font-size:18px;line-height:1}
.plan-price small{font-size:7px;color:var(--muted)}
.plan ul{list-style:none;font-size:10px;color:var(--text)}
.plan li{padding:9px 0;border-bottom:1px solid #e4e4e4;width:150px;margin:0 auto}
.plan .btn{margin-top:20px;background:#fff;border:1px solid #ccc;color:var(--ink);font-size:9px}

/* newsletter */
.newsletter{height:113px;background:var(--blue);text-align:center;color:#fff;padding-top:20px}
.newsletter h2{font-family:"Montserrat",sans-serif;font-size:15px;font-weight:700;text-transform:uppercase}
.newsletter p{font-size:9.5px;color:#e3f1fb;margin:6px auto 10px;width:560px}
.subscribe{display:flex;justify-content:center}
.subscribe .field{width:320px;height:28px;background:#fff;color:#999;font-size:10px;text-align:left;padding:7px 10px}
.subscribe .btn{background:#2a7cb6;color:#fff;height:28px;border-radius:0}

/* footer */
.footer{height:268px;background:var(--footer);color:#999;padding-top:24px;position:relative}
.footer .cols{display:flex;gap:30px}
.footer-col{width:170px;font-size:9.5px;line-height:1.7}
.footer-col h4{font-family:"Montserrat",sans-serif;color:#fff;font-size:11px;text-transform:uppercase;margin-bottom:10px}
.footer-col a{color:var(--blue)}
.footer-col ul{list-style:none}
.footer-col .field{height:22px;background:#2e2e2e;margin:8px 0}
.footer-col .btn{padding:5px 12px;font-size:9px}
.footer-bottom{position:absolute;bottom:0;left:0;right:0;height:54px;border-top:1px solid #2e2e2e}
.footer-bottom .wrap{display:flex;justify-content:space-between;align-items:center;height:54px;font-size:9px}
.cards{display:flex;gap:5px}
.cards i{width:30px;height:18px;background:#e6e6e6;border-radius:2px}
</style>
</head>
<body>

<section class="hero">
  <div class="hero-photo" role="img" aria-label="Photo of a bookshop interior with shelves of records and books"></div>
  <div class="hero-shade"></div>
  <div class="topbar"><div class="wrap"><span>✉ info@amberridgepublishing.com</span><span>♥</span><span>⌕</span></div></div>
  <header class="header"><div class="wrap">
    <div class="logo"><span class="logo-mark"></span>Amber Ridge</div>
    <nav class="nav"><span>Home</span><span>Books</span><span>Text Books</span><span>Audio Books</span><span>Magazines</span><span>Pages</span><span>Blog</span><span>Contact Us</span></nav>
  </div></header>
  <svg class="hero-arrow" style="left:110px" viewBox="0 0 22 40"><path d="M18 4 4 20l14 16" fill="none" stroke="#fff" stroke-width="2"/></svg>
  <svg class="hero-arrow" style="left:1068px" viewBox="0 0 22 40"><path d="M4 4l14 16L4 36" fill="none" stroke="#fff" stroke-width="2"/></svg>
  <div class="hero-copy">
    <h1>Bestseller<br>Upto 50% Off</h1>
    <p>New mystery and fiction titles at half price this season. Find your next favourite read and order it today.</p>
    <span class="btn btn-blue">Buy Now</span>
  </div>
  <div class="welcome-bar"><div class="wrap">
    <div><h2>Welcome to the Amber Ridge Publishing</h2><p>Clean, Responsive and Professional Design with Awesome &amp; Powerful Look</p></div>
    <div class="actions"><span class="btn btn-grey">Start Now</span><span class="btn btn-blue">Buy Now</span></div>
  </div></div>
</section>

<section class="intro"><div class="wrap">
  <h2 class="section-title">Amber Ridge Publishing</h2>
  <div class="title-rule"></div>
  <p class="section-lead">We publish mystery, fiction and stories for readers worldwide. Every book is edited with care, printed well and shipped quickly so the next chapter is never far from your hands.</p>
  <div class="features">
    <div class="feature is-active">
      <div class="icon"><svg width="20" height="20" viewBox="0 0 20 20"><rect x="3" y="8" width="14" height="10" fill="none" stroke="#fff" stroke-width="1.6"/><rect x="2" y="5" width="16" height="4" fill="none" stroke="#fff" stroke-width="1.6"/><path d="M10 5v13" stroke="#fff" stroke-width="1.6"/></svg></div>
      <h3>Free Gift Wrap</h3><p>Every order can be wrapped at no extra cost, ready to give to a friend.</p><span class="btn btn-outline">Read More</span>
    </div>
    <div class="feature">
      <div class="icon"><svg width="20" height="20" viewBox="0 0 20 20"><path d="M3 4h6v13H3zM11 4h6v13h-6z" fill="none" stroke="#666" stroke-width="1.6"/></svg></div>
      <h3>Buy Selling Used Books</h3><p>Trade your read copies and pick up used titles at fair prices.</p><span class="btn btn-outline">Read More</span>
    </div>
    <div class="feature">
      <div class="icon"><svg width="22" height="20" viewBox="0 0 22 20"><rect x="1" y="5" width="12" height="9" fill="none" stroke="#666" stroke-width="1.6"/><path d="M13 8h4l3 3v3h-7z" fill="none" stroke="#666" stroke-width="1.6"/><circle cx="5" cy="16" r="2" fill="#666"/><circle cx="16" cy="16" r="2" fill="#666"/></svg></div>
      <h3>Free Shipping</h3><p>Orders above a small total ship free to most countries worldwide.</p><span class="btn btn-outline">Read More</span>
    </div>
    <div class="feature">
      <div class="icon"><svg width="20" height="20" viewBox="0 0 20 20"><path d="M4 8a6 6 0 0 1 11-2M16 12a6 6 0 0 1-11 2" fill="none" stroke="#666" stroke-width="1.6"/><path d="M15 2v4h-4M5 18v-4h4" fill="none" stroke="#666" stroke-width="1.6"/></svg></div>
      <h3>Returns &amp; Exchange</h3><p>Not the right book? Return or swap it within thirty days.</p><span class="btn btn-outline">Read More</span>
    </div>
  </div>
</div></section>

<section class="bestseller"><div class="wrap">
  <h2 class="section-title">Best <span class="accent">Top</span> Seller</h2>
  <div class="title-rule"></div>
  <p class="section-lead">The titles our readers are talking about this month, picked from our newest releases and most loved stories.</p>
  <div class="book-row">
    <div class="book-card">
      <div class="book-cover" role="img" aria-label="Book cover for Every Quiet Sunday" style="background:linear-gradient(135deg,#d8d4cc,#a9a49b)"></div>
      <h4>Every Quiet Sunday</h4><p class="by">Sarah Lindqvist</p>
      <div class="meta"><span class="price">$28.95</span><span class="stars">★★★★★</span></div>
    </div>
    <div class="book-card is-featured">
      <span class="badge">NEW</span>
      <div class="book-cover" role="img" aria-label="Book cover for Silent Ledger" style="background:linear-gradient(135deg,#3f7fc8,#1d4e8c)"></div>
      <h4>Silent Ledger</h4><p class="by">By M.R. Theodor</p>
      <div class="view-more">VIEW MORE</div>
    </div>
    <div class="book-card">
      <div class="book-cover" role="img" aria-label="Book cover for Ember Lane" style="background:linear-gradient(135deg,#4a3a2e,#1f1a16)"></div>
      <h4>Ember Lane</h4><p class="by">By Nell Hartman</p>
      <div class="meta"><span class="price">$24.75</span><span class="stars">★★★★★</span></div>
    </div>
    <div class="book-card">
      <div class="book-cover" role="img" aria-label="Book cover for Paper Harbor" style="background:linear-gradient(135deg,#3a5a8c,#c9463d)"></div>
      <h4>Paper Harbor</h4><p class="by">By Jane Corliss</p>
      <div class="meta"><span class="price">$24.75</span><span class="stars">★★★★★</span></div>
    </div>
  </div>
  <div class="pager"><span>‹</span><span>1</span><span class="is-current">2</span><span>3</span><span>›</span></div>
</div></section>

<section class="video">
  <div class="video-photo" role="img" aria-label="Photo of a reader with glasses in a library"></div>
  <div class="video-shade"></div>
  <div class="video-copy">
    <h2>Play a Video on Parallax</h2>
    <div class="play"><svg width="14" height="16" viewBox="0 0 14 16"><path d="M2 1l11 7-11 7z" fill="#fff"/></svg></div>
    <p class="sub">Amber Ridge Publishing<small>Stories worth every page</small></p>
  </div>
</section>

<section class="catalog"><div class="wrap">
  <div class="catalog-col">
    <div class="catalog-head"><h3>New Product</h3><div class="arrows"><span>‹</span><span>›</span></div></div>
    <div class="item"><div class="item-cover" role="img" aria-label="Book cover" style="background:linear-gradient(135deg,#2f5fa8,#163a6e)"></div><div><h4>SPINNER CURSE</h4><p class="by">Nora Ashby</p><span class="stars">★★★★★</span><br><span class="tag">$24.00</span><br><span class="add">ADD TO CART ›</span></div></div>
    <div class="item"><div class="item-cover" role="img" aria-label="Book cover" style="background:linear-gradient(135deg,#f0e3c4,#d89a3c)"></div><div><h4>SPINNER CURSE</h4><p class="by">Nora Ashby</p><span class="stars">★★★★★</span><br><span class="tag">$24.00</span><br><span class="add">ADD TO CART ›</span></div></div>
  </div>
  <div class="catalog-col">
    <div class="catalog-head"><h3>Best Seller</h3><div class="arrows"><span>‹</span><span>›</span></div></div>
    <div class="item"><div class="item-cover" role="img" aria-label="Book cover" style="background:linear-gradient(135deg,#4a3a2e,#1f1a16)"></div><div><h4>SPINNER CURSE</h4><p class="by">Nora Ashby</p><span class="stars">★★★★★</span><br><span class="tag">$24.00</span><br><span class="add">ADD TO CART ›</span></div></div>
    <div class="item"><div class="item-cover" role="img" aria-label="Book cover" style="background:linear-gradient(135deg,#e8e2d2,#8d9a6a)"></div><div><h4>SPINNER CURSE</h4><p class="by">Nora Ashby</p><span class="stars">★★★★★</span><br><span class="tag">$24.00</span><br><span class="add">ADD TO CART ›</span></div></div>
  </div>
  <div class="catalog-col">
    <div class="catalog-head"><h3>Pre Order</h3><div class="arrows"><span>‹</span><span>›</span></div></div>
    <div class="item"><div class="item-cover" role="img" aria-label="Book cover" style="background:linear-gradient(135deg,#3a5a8c,#c9463d)"></div><div><h4>SPINNER CURSE</h4><p class="by">Nora Ashby</p><span class="stars">★★★★★</span><br><span class="tag">$24.00</span><br><span class="add">ADD TO CART ›</span></div></div>
    <div class="item"><div class="item-cover" role="img" aria-label="Book cover" style="background:linear-gradient(135deg,#1b1b1b,#d6a23a)"></div><div><h4>SPINNER CURSE</h4><p class="by">Nora Ashby</p><span class="stars">★★★★★</span><br><span class="tag">$24.00</span><br><span class="add">ADD TO CART ›</span></div></div>
  </div>
</div></section>

<section class="testimonials">
  <h2 class="section-title">What Our Client Say About Us</h2>
  <div class="title-rule"></div>
  <div class="people">
    <span class="nav-arrow">‹</span>
    <div class="avatar sm" role="img" aria-label="Reader portrait"></div>
    <div class="avatar lg" role="img" aria-label="Portrait of Delia Marsh"></div>
    <div class="avatar sm" role="img" aria-label="Reader portrait"></div>
    <span class="nav-arrow">›</span>
  </div>
  <p class="name">Delia Marsh</p>
  <p class="role">Book Reviewer</p>
  <p class="quote">Every order arrived quickly and beautifully wrapped. Their mystery list is the best I have found in years of reading.</p>
  <div class="dots"><i class="is-current"></i><i></i><i></i></div>
</section>

<section class="counters"><div class="wrap">
  <div class="counter"><strong>3578</strong><span>Books to Read</span></div>
  <div class="counter"><strong>589</strong><span>Online Users</span></div>
  <div class="counter"><strong>1250</strong><span>Best Authors</span></div>
  <div class="counter"><strong>57</strong><span>Awards</span></div>
</div></section>

<section class="guide"><div class="wrap">
  <h2 class="section-title">The Book Guide <span class="accent">Online</span> Book Store</h2>
  <div class="title-rule"></div>
  <p class="section-lead">Reading notes, author interviews and guides from our editors, written to help you choose the right book for every evening.</p>
  <div class="guide-grid">
    <div class="guide-card"><div class="guide-cover" role="img" aria-label="Book cover for Paper Measures" style="background:linear-gradient(135deg,#f0c23a,#d8442e)"><span class="guide-date">15<i>Mar</i></span></div>
      <div class="guide-body"><p class="by">Posted by the Editor</p><h4>Papilibero Tempore</h4><p>Notes on pacing a mystery and why the quiet chapters matter most.</p><span class="more">SEE MORE ›</span></div></div>
    <div class="guide-card"><div class="guide-cover" role="img" aria-label="Book cover illustration in pink tones" style="background:linear-gradient(135deg,#fbe9e4,#e28b7a)"><span class="guide-date">18<i>Mar</i></span></div>
      <div class="guide-body"><p class="by">Posted by the Editor</p><h4>Papilibero Tempore</h4><p>A short guide to building a reading habit during a busy week.</p><span class="more">SEE MORE ›</span></div></div>
    <div class="guide-card"><div class="guide-cover" role="img" aria-label="Book cover illustration in green and blue" style="background:linear-gradient(135deg,#eef3e0,#6aa3b8)"><span class="guide-date">26<i>Mar</i></span></div>
      <div class="guide-body"><p class="by">Posted by the Editor</p><h4>Papilibero Tempore</h4><p>Our authors share the books that first made them want to write.</p><span class="more">SEE MORE ›</span></div></div>
    <div class="guide-card"><div class="guide-cover" role="img" aria-label="Book cover in red and white" style="background:linear-gradient(135deg,#f4f4f4,#c73a3a)"><span class="guide-date">29<i>Mar</i></span></div>
      <div class="guide-body"><p class="by">Posted by the Editor</p><h4>Papilibero Tempore</h4><p>How a first draft becomes a finished book on your shelf.</p><span class="more">SEE MORE ›</span></div></div>
  </div>
</div></section>

<section class="gift">
  <h2 class="section-title">Book Store Gift Card</h2>
  <div class="wrap">
    <div class="gift-list">
      <div class="gift-item"><h4><i></i>Any Occasion</h4><p>Give the gift of a good story for birthdays, holidays or simply because. Cards never expire and work on every title.</p></div>
      <div class="gift-item is-active"><h4><i></i>Special Occasion</h4><p>Mark weddings and graduations with a card that lets them pick a new shelf of favourites.</p></div>
      <div class="gift-item"><h4><i></i>Cards for Kids</h4><p>Bright cards for young readers, ready to spend on picture books and first chapters.</p></div>
    </div>
  </div>
  <div class="gift-visual" role="img" aria-label="Photo of a laptop showing a reader in a library"></div>
</section>

<section class="pricing"><div class="wrap">
  <h2 class="section-title">Find Your <span class="accent">Best Price</span> Package</h2>
  <div class="title-rule"></div>
  <p class="section-lead">Choose a reading plan that fits you, with monthly books, audio titles and magazines delivered to your door.</p>
  <div class="plans">
    <div class="plan"><div class="plan-head">Personal</div><div class="plan-price"><strong>775</strong><small>/ month</small></div>
      <ul><li>250 E-Books</li><li>50 Comics</li><li>3 Audio</li><li>10 Magazines</li></ul><span class="btn">Purchase Now</span></div>
    <div class="plan"><div class="plan-head">Professional</div><div class="plan-price"><strong>1495</strong><small>/ month</small></div>
      <ul><li>250 E-Books</li><li>50 Comics</li><li>3 Audio</li><li>10 Magazines</li></ul><span class="btn">Purchase Now</span></div>
    <div class="plan"><div class="plan-head">Business</div><div class="plan-price"><strong>1995</strong><small>/ month</small></div>
      <ul><li>250 E-Books</li><li>50 Comics</li><li>3 Audio</li><li>10 Magazines</li></ul><span class="btn">Purchase Now</span></div>
  </div>
</div></section>

<section class="newsletter">
  <h2>Subscribe to Our Newsletter for the Latest News.</h2>
  <p>Get new release dates, author events and member offers sent straight to your inbox every week.</p>
  <div class="subscribe"><span class="field">Enter Your Email Address</span><span class="btn">Subscribe</span></div>
</section>

<footer class="footer">
  <div class="wrap cols">
    <div class="footer-col"><h4>About Us</h4><p>An independent publisher of mystery and fiction for readers around the world.</p><p>12 Orchard Lane, Fairbrook</p><p>+1 555 014 2290</p><p>info@amberridgepublishing.com</p></div>
    <div class="footer-col"><h4>Latest Tweets</h4><p>New mystery arrives this week from <a>@amberridge</a> read the first chapter now.</p><p style="margin-top:8px">Signed copies of Silent Ledger are on sale at <a>@amberridge</a> today.</p></div>
    <div class="footer-col"><h4>Information</h4><ul><li>› Specials</li><li>› New products</li><li>› Best sellers</li><li>› Contact us</li><li>› Terms of use</li><li>› Sitemap</li></ul></div>
    <div class="footer-col"><h4>Newsletter</h4><p>Sign up for news and offers from our editors.</p><div class="field"></div><span class="btn btn-blue">Subscribe</span></div>
  </div>
  <div class="footer-bottom"><div class="wrap"><span>© Amber Ridge Publishing. All rights reserved.</span><div class="cards"><i></i><i></i><i></i><i></i></div></div></div>
</footer>

</body>
</html>
```